Business Card Design

Contact Information for Business Card

A vertical business card request- a medium & light gray with silverfern tree logo (logo is attached)

Please use Trebuchet font -- if possible- can we use two different color gray? (See pictures attached below)
Info on the front should be the Silverfern tree logo - on the top of the card, followed by the info ...
Card to read: " " indicated what should be on the card --
Name: " Joan Pelley "
Title : "Partner "
" Office: 202.555.0147 "
" Mobile: 202.555.0182 "

Backside of the card - solid medium color gray color w/ address and small message centered in the card - Trebuchet font
to read:

" 317 B North Linden Avenue, NE "
" Washington, DC 20099 "

Then below address to read:
" Fundraising | Event Planning | Political Consulting "

```html
<!DOCTYPE html>
<html lang="en">
<head>
<meta charset="utf-8">
<title>Silverfern Strategies – Business Card</title>
<link rel="stylesheet" href="https://fonts.googleapis.com/css2?family=PT+Sans:ital,wght@0,400;0,700;1,700&display=swap">
<style>
  :root {
    --page-bg: #e9e6e1;
    --gray-medium: #6f6f6f;
    --gray-dark: #4f4f4f;
    --gray-light: #c4c4c4;
    --card-white: #f7f7f7;
    --text-dark: #1f1f1f;
    --text-gray: #6a6a6a;
  }
  * { margin: 0; padding: 0; box-sizing: border-box; }
  html, body { width: 1200px; height: 892px; overflow: hidden; }
  body {
    background: var(--page-bg);
    font-family: "PT Sans", "Trebuchet MS", sans-serif;
    display: flex;
    align-items: center;
    justify-content: center;
    gap: 40px;
  }
  .card {
    position: relative;
    width: 540px;
    height: 309px;
    background: var(--card-white);
    box-shadow: 0 6px 18px rgba(0,0,0,0.18);
    overflow: hidden;
  }
  .card-front .split { position: absolute; inset: 0; }
  .brand {
    position: absolute;
    left: 190px;
    top: 16px;
    display: flex;
    align-items: center;
    gap: 12px;
    color: var(--gray-light);
    font-weight: 400;
  }
  .brand-mark {
    width: 30px; height: 30px;
    border-radius: 50%;
    background: var(--card-white);
  }
  .brand-name { font-size: 28px; letter-spacing: 2px; line-height: 1; text-transform: uppercase; }
  .brand-sub { font-size: 13px; letter-spacing: 3px; text-transform: uppercase; margin-top: 3px; }
  .contact {
    position: absolute;
    right: 26px;
    bottom: 16px;
    text-align: right;
    color: var(--text-gray);
  }
  .person-name { font-size: 30px; font-weight: 700; line-height: 1.05; }
  .person-title { font-size: 19px; font-weight: 700; line-height: 1.2; margin-bottom: 8px; }
  .contact-line {
    display: flex;
    justify-content: flex-end;
    align-items: center;
    gap: 10px;
    font-size: 16px;
    line-height: 23px;
  }
  .icon {
    width: 18px; height: 18px;
    background: var(--gray-medium);
    display: inline-flex; align-items: center; justify-content: center;
  }
  .card-back {
    display: flex;
    flex-direction: column;
    align-items: center;
    justify-content: center;
    color: var(--text-dark);
  }
  .address { font-size: 22px; line-height: 34px; text-align: center; }
  .services { margin-top: 34px; font-size: 21px; font-weight: 700; font-style: italic; }
</style>
</head>
<body>
  <section class="card card-front">
    <svg class="split" width="540" height="309" viewBox="0 0 540 309">
      <polygon points="0,0 540,0 540,150 0,30" fill="var(--gray-medium)"/>
      <polygon points="0,30 540,150 540,160 0,40" fill="var(--gray-dark)"/>
    </svg>
    <div class="brand">
      <span class="brand-mark"></span>
      <div>
        <div class="brand-name">Silverfern</div>
        <div class="brand-sub">Strategies</div>
      </div>
    </div>
    <div class="contact">
      <div class="person-name">Joan Pelley</div>
      <div class="person-title">Partner</div>
      <div class="contact-line">202.555.0147
        <span class="icon"><svg width="12" height="12" viewBox="0 0 12 12"><path d="M2 4c0-2 3-2 4-2s4 0 4 2v1H8V4H4v1H2zM3 6h6l1 4H2z" fill="#fff"/></svg></span>
      </div>
      <div class="contact-line">202.555.0182
        <span class="icon"><svg width="12" height="12" viewBox="0 0 12 12"><rect x="3.5" y="1" width="5" height="10" rx="1" fill="#fff"/></svg></span>
      </div>
      <div class="contact-line">joan@silverfernllc.com
        <span class="icon"><svg width="12" height="12" viewBox="0 0 12 12"><rect x="1" y="3" width="10" height="7" fill="#fff"/><path d="M1 3l5 4 5-4" stroke="#6f6f6f" fill="none"/></svg></span>
      </div>
    </div>
  </section>

  <section class="card card-back">
    <div class="address">
      <div>317 B North Linden Avenue, NE</div>
      <div>Washington, DC 20099</div>
    </div>
    <div class="services">" Fundraising | Event Planning | Political Consulting</div>
  </section>
</body>
</html>
```